Redesign of iOS App Lumo Tutor

Redesign of existing App Lumo Tutor, an app that helps learning Japanese Kanjis, Hiragana, Katakana.

The functionallity should remain the same as today: the app is free, you may download it at the app store. But: I like the design of my other apps better ;)

Target Market(s)

Students learning Japanese

Industry/Entity Type

Teacher

Font styles to use
Sans Serif

Requirements
Must have
• Lumo Tutor has 7 main screens, all screens has to be designed for iPhone and iPad: Main, Settings, Reading Tests, Writing Tests, Game, Paper Mode, Search
Nice to have
• I like the logo as it is today

```html
<!DOCTYPE html>
<html lang="en">
<head>
<meta charset="utf-8">
<title>Lumo Tutor — App Redesign</title>
<link href="https://fonts.googleapis.com/css2?family=Roboto:wght@300;400;500&display=swap" rel="stylesheet">
<style>
  :root{
    --stage:#4a4a4a;
    --screen:#ffffff;
    --ink:#222222;
    --muted:#8d8d8d;
    --line:#d6d6d6;
    --pill-dark:#3f3f3f;
    --pill-gray:#8c8c8c;
    --red:#f05a47;
    --blue:#3d9cf0;
    --teal:#1cc3ac;
    --brand:#f05a47;
    --tabbar:#f4f4f4;
    --tab-active:#8a8a8a;
  }
  *{box-sizing:border-box;margin:0;padding:0}
  html,body{width:1200px;height:1200px;overflow:hidden}
  body{background:var(--stage);font-family:"Roboto",sans-serif;color:var(--ink);position:relative}

  .corner-name{position:absolute;right:78px;top:98px;color:#fff;font-size:30px;font-weight:500;letter-spacing:.5px}

  .screen{position:absolute;background:var(--screen);width:385px;height:684px;overflow:hidden}
  .screen--splash{left:152px;top:166px}
  .screen--main{left:598px;top:341px}

  .status{position:absolute;left:0;top:0;width:100%;height:18px;font-size:10.5px;color:#555;font-weight:400}
  .status__signal{position:absolute;left:7px;top:5px;display:flex;gap:1.5px}
  .status__signal i{width:5px;height:5px;border-radius:50%;background:#555;display:block}
  .status__carrier{position:absolute;left:47px;top:3px}
  .status__time{position:absolute;left:0;right:0;top:2px;text-align:center}
  .status__right{position:absolute;right:8px;top:2px;display:flex;align-items:center;gap:5px}
  .battery{width:24px;height:9px;border:1px solid #555;border-radius:2px;padding:1px;position:relative}
  .battery::after{content:"";position:absolute;right:-3px;top:2px;width:2px;height:3px;background:#555}
  .battery span{display:block;width:100%;height:100%;background:#555}

  .splash__mark{position:absolute;left:152px;top:300px;width:80px;height:80px;background:var(--brand);border-radius:6px}
  .splash__name{position:absolute;left:0;right:0;top:402px;text-align:center;font-size:14px;letter-spacing:.3px;color:var(--ink)}

  .levels{position:absolute;top:50px;left:0;width:100%;height:30px}
  .levels__tab{position:absolute;top:0;font-size:18px;font-weight:300;color:var(--muted);transform:translateX(-50%)}
  .levels__tab--active{color:var(--ink);font-weight:400}
  .levels__underline{position:absolute;left:12px;top:28px;width:32px;height:2px;background:var(--ink)}

  .legend{position:absolute;top:98px;left:0;width:100%;height:20px}
  .legend svg{position:absolute;top:0;transform:translateX(-50%)}

  .tests{position:absolute;top:124px;left:14px;width:358px}
  .test{height:59px;position:relative;border-bottom:1px solid var(--line)}
  .test__label{position:absolute;left:3px;top:1px;font-size:9px;color:var(--ink)}
  .pill{position:absolute;top:16px;height:20px;border-radius:10px;color:#fff;font-size:9px;display:flex;align-items:center;justify-content:center;border:1px solid rgba(0,0,0,.12)}
  .pill--total{left:0;width:60px;background:var(--pill-dark)}
  .pill--pending{left:100px;width:61px;background:var(--pill-gray)}
  .pill--wrong{left:168px;width:60px;background:var(--red)}
  .pill--unsure{left:236px;width:60px;background:var(--blue)}
  .pill--known{left:304px;width:60px;background:var(--teal)}
  .test__action{position:absolute;left:74px;top:21px;font-size:8px;color:#666}

  .tabbar{position:absolute;left:0;bottom:0;width:100%;height:49px;display:grid;grid-template-columns:repeat(5,1fr);background:var(--tabbar);border-top:1px solid #cfcfcf}
  .tabbar__item{display:flex;flex-direction:column;align-items:center;justify-content:center;gap:2px;font-size:7.5px;color:#888;border-left:1px solid #cfcfcf}
  .tabbar__item:first-child{border-left:none}
  .tabbar__item--active{background:var(--tab-active);color:#fff}
</style>
</head>
<body>

<div class="corner-name">Lumo Tutor</div>

<section class="screen screen--splash">
  <div class="status">
    <div class="status__signal"><i></i><i></i><i></i><i></i><i></i></div>
    <span class="status__carrier">Nexa</span>
    <span class="status__time">9:41 AM</span>
    <div class="status__right"><span>⟳ ➤ ⏰</span><span>100%</span><div class="battery"><span></span></div></div>
  </div>
  <div class="splash__mark"></div>
  <div class="splash__name">LUMO TUTOR</div>
</section>

<section class="screen screen--main">
  <div class="status">
    <div class="status__signal"><i></i><i></i><i></i><i></i><i></i></div>
    <span class="status__carrier">Nexa</span>
    <span class="status__time">9:41 AM</span>
    <div class="status__right"><span>⟳ ➤ ⏰</span><span>100%</span><div class="battery"><span></span></div></div>
  </div>

  <nav class="levels">
    <span class="levels__tab levels__tab--active" style="left:27px">K</span>
    <span class="levels__tab" style="left:82px">N5</span>
    <span class="levels__tab" style="left:137px">N4</span>
    <span class="levels__tab" style="left:192px">N3</span>
    <span class="levels__tab" style="left:247px">N2</span>
    <span class="levels__tab" style="left:302px">N1</span>
    <svg class="levels__tab" style="left:357px;top:4px" width="14" height="14" viewBox="0 0 24 24"><path fill="#8d8d8d" d="M12 2l3 7 7 .6-5.4 4.7 1.7 7.2L12 17.6 5.7 21.5l1.7-7.2L2 9.6 9 9z"/></svg>
    <div class="levels__underline"></div>
  </nav>

  <div class="legend">
    <svg style="left:145px" width="16" height="18" viewBox="0 0 16 18"><path d="M2 2l12 7-12 7z" fill="none" stroke="#777" stroke-width="1.3"/></svg>
    <svg style="left:212px" width="16" height="16" viewBox="0 0 16 16"><path d="M2 2l12 12M14 2L2 14" stroke="var(--red)" stroke-width="1.5"/></svg>
    <svg style="left:280px" width="18" height="18" viewBox="0 0 18 18"><circle cx="9" cy="9" r="7.5" fill="none" stroke="var(--blue)" stroke-width="1.3"/></svg>
    <svg style="left:353px" width="18" height="18" viewBox="0 0 18 18"><path d="M2 10l5 5L17 2" fill="none" stroke="var(--teal)" stroke-width="1.3"/></svg>
  </div>

  <div class="tests">
    <div class="test"><span class="test__label">Hiragana - Reading</span><span class="pill pill--total">71</span><span class="test__action">Test</span><span class="pill pill--pending">71</span><span class="pill pill--wrong">0</span><span class="pill pill--unsure">0</span><span class="pill pill--known">0</span></div>
    <div class="test"><span class="test__label">Reading - Hiragana</span><span class="pill pill--total">71</span><span class="test__action">Test</span><span class="pill pill--pending">71</span><span class="pill pill--wrong">0</span><span class="pill pill--unsure">0</span><span class="pill pill--known">0</span></div>
    <div class="test"><span class="test__label">Hiragana - Writing</span><span class="pill pill--total">71</span><span class="test__action">Test</span><span class="pill pill--pending">71</span><span class="pill pill--wrong">0</span><span class="pill pill--unsure">0</span><span class="pill pill--known">0</span></div>
    <div class="test"><span class="test__label">Katakana - Reading</span><span class="pill pill--total">71</span><span class="test__action">Test</span><span class="pill pill--pending">71</span><span class="pill pill--wrong">0</span><span class="pill pill--unsure">0</span><span class="pill pill--known">0</span></div>
    <div class="test"><span class="test__label">Reading - Katakana</span><span class="pill pill--total">71</span><span class="test__action">Test</span><span class="pill pill--pending">71</span><span class="pill pill--wrong">0</span><span class="pill pill--unsure">0</span><span class="pill pill--known">0</span></div>
    <div class="test"><span class="test__label">Katakana - writing</span><span class="pill pill--total">71</span><span class="test__action">Test</span><span class="pill pill--pending">71</span><span class="pill pill--wrong">0</span><span class="pill pill--unsure">0</span><span class="pill pill--known">0</span></div>
    <div class="test"><span class="test__label">All Test</span><span class="pill pill--total">71</span><span class="test__action">Test</span><span class="pill pill--pending">71</span><span class="pill pill--wrong">0</span><span class="pill pill--unsure">0</span><span class="pill pill--known">0</span></div>
  </div>

  <nav class="tabbar">
    <div class="tabbar__item tabbar__item--active">
      <svg width="26" height="24" viewBox="0 0 26 24"><path d="M2 12L13 2l11 10M5 10v12h6v-7h4v7h6V10" fill="none" stroke="#fff" stroke-width="1.4"/></svg>Home</div>
    <div class="tabbar__item">
      <svg width="24" height="24" viewBox="0 0 24 24"><circle cx="12" cy="12" r="8" fill="none" stroke="#777" stroke-width="1.3" stroke-dasharray="4 2"/><circle cx="12" cy="12" r="3.5" fill="none" stroke="#777" stroke-width="1.3"/></svg>Settings</div>
    <div class="tabbar__item">
      <svg width="24" height="24" viewBox="0 0 24 24"><circle cx="10" cy="10" r="7.5" fill="none" stroke="#777" stroke-width="1.3"/><path d="M15.5 15.5L22 22" stroke="#777" stroke-width="1.3"/></svg>Search</div>
    <div class="tabbar__item">
      <svg width="24" height="24" viewBox="0 0 24 24" fill="none" stroke="#777" stroke-width="1"><rect x="1" y="1" width="6" height="6"/><rect x="9" y="1" width="6" height="6"/><rect x="17" y="1" width="6" height="6"/><rect x="1" y="9" width="6" height="6"/><rect x="9" y="9" width="6" height="6"/><rect x="17" y="9" width="6" height="6"/><rect x="1" y="17" width="6" height="6" fill="#777"/><rect x="9" y="17" width="6" height="6"/><rect x="17" y="17" width="6" height="6"/></svg>Game</div>
    <div class="tabbar__item">
      <svg width="20" height="24" viewBox="0 0 20 24" fill="none" stroke="#777" stroke-width="1.3"><rect x="2" y="1" width="16" height="22"/><path d="M6 7h8M6 11h8M6 15h8"/></svg>Paper</div>
  </nav>
</section>

</body>
</html>
```